Statement of Professional Excellence

Our school community has create a statement of Professional Excellence at our school (LAM = The Linden Academy at Marbury) This will be shared internally and with candidates interviewing at our school. We'd like a branded graphic that lists in an interesting way our statements:

Professional Excellence at LAM

We honor the whole child while embracing them where they are.
We are mission-driven individuals whose dedication to our students motivates our daily work.
We bring flexible thinking to allow the needs of the students to drive the learning.
We are patient, nurturing, empathetic, and compassionate people.
We value, trust, and support each other.
We learn and we teach.
We lean into and celebrate diversity.
We build trust through genuine partnerships with families.
We are quirky, fun and proud of it.

```html
<!DOCTYPE html>
<html lang="en">
<head>
<meta charset="utf-8">
<title>Professional Excellence – The Linden Academy at Marbury</title>
<link rel="stylesheet" href="https://fonts.googleapis.com/css2?family=Crimson+Pro:wght@600;700&family=Fira+Sans:ital,wght@1,500&display=swap">
<style>
  :root {
    --backdrop: #e4e5e7;
    --paper: #f7f7f8;
    --navy: #142a4a;
    --navy-deep: #0f2340;
    --gold: #c9a227;
    --disc: #f3f3f3;
    --card-text: #f1f2f4;
  }
  * { box-sizing: border-box; margin: 0; padding: 0; }
  html, body {
    width: 1180px; height: 1200px; overflow: hidden;
    background: var(--backdrop);
  }
  .sheet {
    position: absolute; left: 138px; top: 10px;
    width: 904px; height: 1180px;
    background: var(--paper);
  }
  .sheet-title {
    position: absolute; left: 26px; top: 44px;
    font-family: "Crimson Pro", Georgia, serif;
    font-weight: 700; font-variant: small-caps;
    font-size: 76px; line-height: 64px;
    color: var(--navy); letter-spacing: 0.5px;
  }
  .school-name {
    position: absolute; right: 50px; top: 70px;
    width: 330px; text-align: center;
    font-family: "Crimson Pro", Georgia, serif;
    font-weight: 600; font-size: 36px; line-height: 38px;
    color: var(--navy);
  }
  .value-grid {
    position: absolute; left: 25px; top: 190px;
    display: grid;
    grid-template-columns: repeat(3, 273px);
    grid-template-rows: repeat(3, 310px);
    gap: 18px;
  }
  .value-card {
    position: relative;
    background: linear-gradient(180deg, var(--navy) 0%, var(--navy-deep) 100%);
    display: flex; flex-direction: column; align-items: center;
  }
  .value-badge {
    position: relative; width: 92px; height: 92px; margin-top: 38px;
  }
  .sprig {
    position: absolute; left: -44px; top: -16px;
    width: 80px; height: 44px; border-radius: 40px 40px 40px 4px;
    background: var(--gold);
  }
  .value-number {
    position: absolute; inset: 0; border-radius: 50%;
    background: var(--disc);
    display: flex; align-items: center; justify-content: center;
    font-family: "Crimson Pro", Georgia, serif; font-weight: 700;
    font-size: 76px; line-height: 1; color: var(--gold);
    padding-bottom: 4px;
  }
  .value-text {
    flex: 1; display: flex; align-items: center; justify-content: center;
    padding: 0 24px 40px; text-align: center;
    font-family: "Fira Sans", Arial, sans-serif; font-style: italic; font-weight: 500;
    font-size: 20px; line-height: 27px; color: var(--card-text);
  }
  .value-text.upper { align-items: flex-start; padding-top: 16px; }
</style>
</head>
<body>
  <main class="sheet">
    <h1 class="sheet-title">Professional<br>Excellence</h1>
    <div class="school-name">The Linden Academy at Marbury</div>

    <section class="value-grid">
      <article class="value-card">
        <div class="value-badge"><span class="sprig" role="img" aria-label="Gold olive sprig"></span><span class="value-number">1</span></div>
        <p class="value-text upper">We honor the whole child while embracing them where they are.</p>
      </article>
      <article class="value-card">
        <div class="value-badge"><span class="sprig" role="img" aria-label="Gold olive sprig"></span><span class="value-number">2</span></div>
        <p class="value-text upper">We are mission-driven individuals whose dedication to our students motivates our daily work.</p>
      </article>
      <article class="value-card">
        <div class="value-badge"><span class="sprig" role="img" aria-label="Gold olive sprig"></span><span class="value-number">3</span></div>
        <p class="value-text upper">We bring flexible thinking to allow the needs of the students to drive the learning.</p>
      </article>
      <article class="value-card">
        <div class="value-badge"><span class="sprig" role="img" aria-label="Gold olive sprig"></span><span class="value-number">4</span></div>
        <p class="value-text">We are patient, nurturing, empathetic, and compassionate people.</p>
      </article>
      <article class="value-card">
        <div class="value-badge"><span class="sprig" role="img" aria-label="Gold olive sprig"></span><span class="value-number">5</span></div>
        <p class="value-text">We value, trust, and support each other.</p>
      </article>
      <article class="value-card">
        <div class="value-badge"><span class="sprig" role="img" aria-label="Gold olive sprig"></span><span class="value-number">6</span></div>
        <p class="value-text">We learn and we teach.</p>
      </article>
      <article class="value-card">
        <div class="value-badge"><span class="sprig" role="img" aria-label="Gold olive sprig"></span><span class="value-number">7</span></div>
        <p class="value-text">We lean into and celebrate diversity.</p>
      </article>
      <article class="value-card">
        <div class="value-badge"><span class="sprig" role="img" aria-label="Gold olive sprig"></span><span class="value-number">8</span></div>
        <p class="value-text">We build trust through genuine partnerships with families.</p>
      </article>
      <article class="value-card">
        <div class="value-badge"><span class="sprig" role="img" aria-label="Gold olive sprig"></span><span class="value-number">9</span></div>
        <p class="value-text">We are quirky, fun and proud of it.</p>
      </article>
    </section>
  </main>
</body>
</html>
```